Lumen Harbor Business Card Design Project

We have recently rebranded and would like to design new business cards that incorporate the corporate logo - double sided cards with corporate logo on one side and contact details on the other

Target Market(s)

Sophisticated and high net worth investors and finance industry professionals

Industry/Entity Type

Funds Management

Contact Information for Business Card

The card should prominently feature the company name and logo. Other details will be standard contact details for each staff member - name, address, phone, email, website

Colors
0054AA
0677BA
7BADD7
CADEEF
E8F1F8

Requirements
Must have
• Double-sided design with one side prominently featuring the corporate logo and the other side with all standard contact details

```html
<!DOCTYPE html>
<html lang="en">
<head>
<meta charset="utf-8">
<title>Lumen Harbor – Business Card</title>
<link rel="stylesheet" href="https://fonts.googleapis.com/css2?family=Cinzel:wght@400;600&family=Arimo:wght@400&display=swap">
<style>
  :root {
    --stage: #2a2b2d;
    --card: #21467a;
    --card-tint: #27528b;
    --card-edge: #1d3f6f;
    --ink: #ffffff;
    --shadow: rgba(0, 0, 0, 0.55);
  }
  * { margin: 0; padding: 0; box-sizing: border-box; }
  html, body {
    width: 1200px;
    height: 1015px;
    overflow: hidden;
    background: var(--stage);
  }
  .sheet {
    width: 1200px;
    height: 1015px;
    display: flex;
    flex-direction: column;
    align-items: center;
    justify-content: center;
    gap: 44px;
  }
  .card {
    position: relative;
    width: 640px;
    height: 366px;
    background: var(--card);
    color: var(--ink);
    box-shadow: 0 14px 30px var(--shadow);
    overflow: hidden;
  }

  /* Front */
  .card-front {
    display: flex;
    align-items: center;
    justify-content: center;
  }
  .brand {
    display: flex;
    align-items: center;
    gap: 18px;
  }
  .brand-mark {
    width: 40px;
    height: 40px;
    border-radius: 50%;
    background: var(--ink);
    flex: none;
  }
  .wordmark {
    font-family: "Cinzel", serif;
    font-weight: 600;
    font-size: 48px;
    letter-spacing: 2px;
    line-height: 1;
    color: var(--ink);
  }

  /* Back */
  .card-back {
    font-family: "Arimo", sans-serif;
  }
  .brand-emboss {
    position: absolute;
    top: 46px;
    right: 56px;
    width: 170px;
    height: 170px;
    border-radius: 50%;
    background: var(--card-tint);
    border: 1px solid var(--card-edge);
  }
  .details {
    position: absolute;
    left: 64px;
    top: 96px;
  }
  .holder-name {
    font-family: "Cinzel", serif;
    font-weight: 400;
    font-size: 25px;
    letter-spacing: 1px;
    line-height: 1;
  }
  .holder-role {
    font-size: 16px;
    line-height: 20px;
    margin-top: 6px;
  }
  .contact-list {
    list-style: none;
    margin-top: 28px;
    font-size: 16px;
    line-height: 23px;
  }
  .contact-list li {
    display: flex;
    align-items: center;
    gap: 8px;
  }
  .contact-icon {
    width: 15px;
    height: 15px;
    flex: none;
  }
  .address {
    margin-top: 28px;
    font-size: 16px;
    line-height: 21px;
    font-style: normal;
  }
</style>
</head>
<body>
<main class="sheet">
  <section class="card card-front" aria-label="Card front">
    <div class="brand">
      <span class="brand-mark" aria-hidden="true"></span>
      <h1 class="wordmark">Lumen Harbor</h1>
    </div>
  </section>

  <section class="card card-back" aria-label="Card back">
    <span class="brand-emboss" aria-hidden="true"></span>
    <div class="details">
      <h2 class="holder-name">Daniel Mercer</h2>
      <p class="holder-role">Managing Director</p>
      <ul class="contact-list">
        <li>
          <svg class="contact-icon" viewBox="0 0 16 16" aria-hidden="true">
            <path d="M3.5 1.5l2.3 2.7-1.3 1.6a9 9 0 0 0 5.7 5.7l1.6-1.3 2.7 2.3-1.7 2a11 11 0 0 1-11.2-11.2z" fill="#fff"/>
          </svg>
          <span>044-555 201 337</span>
        </li>
        <li>
          <svg class="contact-icon" viewBox="0 0 16 16" aria-hidden="true">
            <rect x="1" y="3.5" width="14" height="9.5" fill="#fff"/>
            <path d="M1 3.5l7 5.5 7-5.5" fill="none" stroke="#21467a" stroke-width="1.3"/>
          </svg>
          <span>hello@lumenharbor.com</span>
        </li>
        <li>
          <svg class="contact-icon" viewBox="0 0 16 16" aria-hidden="true">
            <circle cx="8" cy="8" r="6.5" fill="none" stroke="#fff" stroke-width="1.4"/>
            <ellipse cx="8" cy="8" rx="2.8" ry="6.5" fill="none" stroke="#fff" stroke-width="1.2"/>
            <path d="M1.5 8h13M2.6 4.7h10.8M2.6 11.3h10.8" stroke="#fff" stroke-width="1.1"/>
          </svg>
          <span>www.lumenharbor.com</span>
        </li>
      </ul>
      <address class="address">
        421, Address line goes here<br>
        45452, Country Name
      </address>
    </div>
  </section>
</main>
</body>
</html>
```